Business Card Design Project

We need a business card design for a new construction company called 'KORVA HOLDINGS PTY.LTD' We run a construction based company for high end market homes in melbourne, we want something that looks professional and eye catching.The card needs to have a strong design to it something modern as the company name explains "korva." The final design should communicate professionalism and a strong image to our customers on the quality of our work.
On the business card i need
Name: Marek Holtvay
Mob:0417295031
Email:korva.holdings@mailbrook.example
Domestic/Residential/Commercial

```html
<!DOCTYPE html>
<html lang="en">
<head>
<meta charset="utf-8">
<title>Korva Holdings Business Card</title>
<link rel="stylesheet" href="https://fonts.googleapis.com/css2?family=Montserrat:wght@500;600;700&family=Questrial&display=swap">
<style>
  :root {
    --backdrop: #3a3a3a;
    --card-white: #ffffff;
    --ink: #1d1d1d;
    --brand-red: #e3262c;
    --brand-red-deep: #b5161b;
    --on-red: #ffffff;
  }
  * { box-sizing: border-box; margin: 0; padding: 0; }
  html, body {
    width: 1200px;
    height: 1065px;
    overflow: hidden;
    background: var(--backdrop);
  }
  .stage {
    position: relative;
    width: 1200px;
    height: 1065px;
  }
  .card {
    position: absolute;
    left: 220px;
    width: 760px;
    height: 434px;
    border-radius: 24px;
    overflow: hidden;
    box-shadow: 0 14px 30px rgba(0,0,0,0.35);
  }
  /* Front card */
  .card-front {
    top: 66px;
    background: var(--card-white);
  }
  .front-brand {
    position: absolute;
    left: 56px;
    top: 52px;
  }
  .brand-name {
    font-family: "Montserrat", sans-serif;
    font-weight: 700;
    font-size: 68px;
    line-height: 1;
    letter-spacing: -1px;
    color: var(--ink);
  }
  .brand-legal {
    font-family: "Montserrat", sans-serif;
    font-weight: 600;
    font-size: 11px;
    letter-spacing: 4.2px;
    color: var(--brand-red);
    margin-top: 6px;
  }
  .holder {
    position: absolute;
    left: 56px;
    top: 214px;
    font-family: "Questrial", sans-serif;
  }
  .holder-name {
    font-size: 34px;
    color: var(--brand-red);
    line-height: 1.1;
  }
  .holder-services {
    font-size: 15px;
    color: var(--ink);
    margin-top: 8px;
  }
  .contact-list {
    list-style: none;
    margin-top: 22px;
    font-size: 17px;
    color: var(--brand-red);
    line-height: 1.55;
  }
  .contact-label {
    display: inline-block;
    width: 28px;
  }
  /* Back card */
  .card-back {
    top: 566px;
    background: radial-gradient(ellipse at 50% 40%, var(--brand-red) 0%, var(--brand-red-deep) 100%);
    display: flex;
    flex-direction: column;
    align-items: center;
    justify-content: center;
    color: var(--on-red);
  }
  .card-back .brand-name {
    color: var(--on-red);
    font-size: 104px;
  }
  .card-back .brand-legal {
    color: var(--on-red);
    font-size: 17px;
    letter-spacing: 9px;
    margin-top: 8px;
  }
  .back-services {
    font-family: "Montserrat", sans-serif;
    font-weight: 600;
    font-size: 18px;
    margin-top: 10px;
    letter-spacing: 0.5px;
  }
</style>
</head>
<body>
<main class="stage">
  <section class="card card-front">
    <div class="front-brand">
      <div class="brand-name">korva</div>
      <div class="brand-legal">KORVA HOLDINGS PTY.LTD</div>
    </div>
    <div class="holder">
      <p class="holder-name">Marek Holtvay</p>
      <p class="holder-services">Domestic | Residential | Commercial</p>
      <ul class="contact-list">
        <li><span class="contact-label">T |</span>0417 295 031</li>
        <li><span class="contact-label">E |</span>korva.holdings@mailbrook.example</li>
      </ul>
    </div>
  </section>

  <section class="card card-back">
    <div class="brand-name">korva</div>
    <div class="brand-legal">KORVA HOLDINGS PTY.LTD</div>
    <p class="back-services">Domestic | Residential | Commercial</p>
  </section>
</main>
</body>
</html>
```